Senior care homes needs brochure design

I need a brochure design for a senior care home business, the company is based in Long Beach but have care houses in Long Beach and Huntington Beach California. We provide assisted living, independent living care for senior in a residential home. The name of the company is Willowmere Lodges Inc. I would like to see designs that will go well with the color of my Logo that I will be attaching, I will need to add photos or houses, rooms, backyards. also I am thinking in the middle of the inside the services that we provide. The final design should communicate a caring home where anyone can trust their loved ones to us. I would like to incorporate the last picture of my grandpa if possible in a small picture. Under the Dorrance Map I want Facility # 418273915 and under Ashby Map I want Facility #

Baby boomers and older adults

Residential

• must be able to add pictures and move content around

```html
<!DOCTYPE html>
<html lang="en">
<head>
<meta charset="utf-8">
<title>Willowmere Lodges – Tri-fold Brochure</title>
<link href="https://fonts.googleapis.com/css2?family=Crimson+Text:ital,wght@0,400;0,600;1,400&display=swap" rel="stylesheet">
<style>
  :root {
    --page-bg: #eef0f2;
    --paper: #ffffff;
    --fold-grey: #ececec;
    --sky: #4aa8d8;
    --sky-deep: #3d9bd0;
    --sky-light: #8fd0f0;
    --teal: #1f8a8a;
    --ink: #1a1a1a;
    --white: #ffffff;
    --photo-warm: #b98a63;
    --photo-garden: #7fae5e;
    --photo-sky: #b9d7ea;
  }
  * { box-sizing: border-box; margin: 0; padding: 0; }
  html, body { width: 1200px; height: 1080px; overflow: hidden; }
  body { background: var(--page-bg); font-family: "Crimson Text", Georgia, serif; color: var(--ink); }

  .brochure {
    position: absolute; left: 30px; top: 90px;
    width: 1140px; height: 900px;
    background: var(--paper);
    box-shadow: 0 10px 30px rgba(0,0,0,.15);
    overflow: hidden;
  }
  .brochure__backdrop { position: absolute; inset: 0; }
  .panel { position: absolute; top: 0; width: 380px; height: 900px; }
  .panel--left { left: 0; }
  .panel--center { left: 380px; }
  .panel--right { left: 760px; }

  .photo { position: absolute; border: 4px solid var(--white); box-shadow: 0 2px 6px rgba(0,0,0,.2); }
  .photo--round { border-radius: 50%; }
  .photo--living { left: 38px; top: 80px; width: 118px; height: 118px; background: radial-gradient(circle at 40% 45%, #d9c3a8, var(--photo-warm) 70%, #7a4f35); }
  .photo--portrait { left: 128px; top: 124px; width: 58px; height: 58px; background: radial-gradient(circle, #e6d5c2, #b8a28a); }
  .photo--patio { left: 95px; top: 200px; width: 160px; height: 160px; background: linear-gradient(180deg, #e2673a 0%, #d86a3e 30%, var(--photo-garden) 65%, #5d8d45 100%); }
  .photo--yard { left: 50px; top: 260px; width: 300px; height: 142px; border-radius: 14px; background: linear-gradient(180deg, var(--photo-sky) 0%, #e9e2d2 45%, #c6a884 60%, var(--photo-garden) 80%, #5f9a48 100%); }

  .left-copy { position: absolute; left: 36px; top: 408px; width: 300px; text-align: center; color: var(--white); }
  .left-copy__lead { font-size: 15px; line-height: 1.2; margin-bottom: 8px; }
  .left-copy__text { font-style: italic; font-size: 12.5px; line-height: 1.25; margin-bottom: 10px; }

  .center-title { position: absolute; left: 0; top: 58px; width: 380px; text-align: center; font-size: 40px; font-weight: 400; color: var(--sky); }
  .center-intro { position: absolute; left: 26px; top: 128px; width: 328px; font-size: 14.5px; line-height: 1.15; text-align: justify; }
  .center-quote { position: absolute; left: 0; top: 312px; width: 380px; text-align: center; font-size: 38px; line-height: 1.2; color: var(--white); }
  .center-copy { position: absolute; left: 28px; top: 452px; width: 324px; color: var(--white); font-size: 13.5px; line-height: 1.15; }
  .center-copy p { margin-bottom: 10px; }

  .brand { position: absolute; left: 0; top: 112px; width: 380px; display: flex; flex-direction: column; align-items: center; gap: 12px; }
  .brand__dot { width: 46px; height: 46px; border-radius: 50%; background: var(--teal); }
  .brand__name { font-size: 20px; font-weight: 600; letter-spacing: 1.5px; color: var(--ink); text-transform: uppercase; }

  .right-copy { position: absolute; left: 22px; top: 470px; width: 330px; color: var(--white); font-size: 13.5px; line-height: 1.15; }
  .right-copy p { margin-bottom: 10px; }
</style>
</head>
<body>
<main class="brochure">
  <svg class="brochure__backdrop" width="1140" height="900" viewBox="0 0 1140 900" aria-hidden="true">
    <defs>
      <linearGradient id="band" x1="0" y1="0" x2="0" y2="1">
        <stop offset="0" stop-color="#3d9bd0"/>
        <stop offset="1" stop-color="#6cc0ea"/>
      </linearGradient>
    </defs>
    <rect x="380" y="0" width="380" height="900" fill="#ececec"/>
    <path d="M0,330 Q300,250 600,262 T1140,300" fill="none" stroke="#d5d9dd" stroke-width="1.5"/>
    <path d="M0,345 Q300,270 600,280 T1140,320" fill="none" stroke="#e0e3e6" stroke-width="1"/>
    <path d="M0,370 Q320,285 620,300 T1140,360 L1140,800 L0,800 Z" fill="url(#band)"/>
    <rect x="380" y="800" width="380" height="100" fill="#ececec"/>
    <line x1="380" y1="0" x2="380" y2="900" stroke="rgba(0,0,0,.06)"/>
    <line x1="760" y1="0" x2="760" y2="900" stroke="rgba(0,0,0,.06)"/>
  </svg>

  <section class="panel panel--left">
    <div class="photo photo--round photo--living" role="img" aria-label="Photo of a cosy living room with sofas and a brick fireplace"></div>
    <div class="photo photo--round photo--portrait" role="img" aria-label="Small portrait photo of a smiling grandfather"></div>
    <div class="photo photo--round photo--patio" role="img" aria-label="Photo of a backyard patio with orange umbrella, table and chairs"></div>
    <div class="left-copy">
      <p class="left-copy__lead">Duis euismod tempor libero.<br>Nullam ornare pellentesque elit.</p>
      <p class="left-copy__text">Nunc malesuada. Lorem ipsum dolor sit amet, consectetuer adipiscing elit. Duis at ligula. Sed feugiat sodales odio. Proin interdum quam a nunc convallis placerat. Nam leo. Aenean iaculis hendrerit enim. Aliquam lacinia, leo sed sollicitudin rutrum, mi sem porttitor nisl, non mattis magna sapien non diam. Proin nec eros aliquam felis rutrum posuere. Duis euismod tempor libero. Nullam ornare pellentesque elit.</p>
      <p class="left-copy__text">Quisque sit amet arcu. Etiam vitae quam. Vivamus est augue, porta sit amet, consectetuer quis, dapibus id, pede. Aenean convallis.</p>
    </div>
  </section>

  <section class="panel panel--center">
    <h1 class="center-title">Curabitur porttitor.</h1>
    <p class="center-intro">Maecenas non dolor. Vivamus id dui. Donec imperdiet dui lectus. Lorem ipsum dolor sit amet, consectetuer adipiscing elit. Suspendisse consequat nisl ut pede. Vestibulum nonummy dui quis risus. Cras egestas arcu. Quisque quam orci, elementum sit amet, semper ac, vehicula ut, urna. Orbi nec lacus. Phasellus non pede. Fusce risus pede, condimentum quis, faucibus non, felis.</p>
    <blockquote class="center-quote">“Cras sollicitudin sem nec ipsum.”</blockquote>
    <div class="center-copy">
      <p>Duis facilisis. Nullam nunc risus, vehicula sit amet, placerat vel, elementum a, nisl. Nulla tempus luctus orci. Donec condimentum porta lorem. Etiam semper felis ut massa suscipit facilisis. Fusce quis nunc. Ut aliquet auctor est. Pellentesque habitant morbi tristique senectus et netus et malesuada fames ac turpis egestas.</p>
      <p>Quisque congue cursus arcu. In magna libero, egestas vel, tempus eu, suscipit in, metus. Mauris tortor felis, imperdiet vel, vestibulum sit amet, tempus a, lorem. Nam commodo aliquet risus. Nulla vehicula, magna in adipiscing ornare, sem massa volutpat justo, sed accumsan enim quam.</p>
    </div>
  </section>

  <section class="panel panel--right">
    <div class="brand">
      <span class="brand__dot"></span>
      <span class="brand__name">Willowmere Lodges</span>
    </div>
    <div class="photo photo--yard" role="img" aria-label="Photo of a home backyard with lawn, patio umbrella and flowering shrubs"></div>
    <div class="right-copy">
      <p>Tincidunt est. Fusce pede tortor, adipiscing eu, dictum ac, varius sed, nulla.</p>
      <p>Class aptent taciti sociosqu ad litora torquent per conubia nostra, per inceptos hymenaeos. Nam euismod ligula et mauris. Suspendisse imperdiet sem non lacus. Nulla vel risus sed justo lobortis aliquet. Maecenas at orci. Pellentesque habitant morbi tristique senectus et netus et malesuada fames ac turpis egestas. Mauris aliquam egestas purus. Vivamus arcu.</p>
      <p>Donec mollis, elit sed tincidunt commodo, sem diam volutpat nunc, eget interdum nibh libero ut magna.</p>
    </div>
  </section>
</main>
</body>
</html>
```